依頼詳細
瓶の容量は330mlで、茶色の瓶で、王冠はシルバーです。(瓶の写真を添付します)
アルコール度数は7%で非加熱処理なので、ドライですっきりとした飲み口のシードルです。
食中酒としてもご利用いただけます。
販売価格は650円(税込み)です。

弊社店舗のロゴも添付しますのでラベルデザインにおいてご活用ください。
また記載いただきたい文字情報として以下の情報をお取り扱いください。

商品名:Mavolt CIDER
その他1:The Genuine Brisk & Tap Hard Cider Alc.7%
その他2:APPLE 100% natural
その他2:Harvested and Brewed in HIROSAKI,AOMORI,JAPAN

記載項目
ラベルサイズは縦8センチ×横7センチくらいをを基準にご提案ください。
希望イメージ
シンプル 複雑
単色 カラフル
暗い 明るい
日常 高級
遊び心 厳粛
未来的 伝統的
女性的 男性的
希望する色
茶系
納品ファイル
• 高解像度JPG (.jpg)
• イラストレーター形式 (.ai)

視認性も非常によく、シードルの爽やかな印象をデザインに投影いただきました。

皆様、この度はたくさんのご提案まことにありがとうございます。
心より御礼申し上げます。

```html
<!DOCTYPE html>
<html lang="en">
<head>
<meta charset="UTF-8">
<title>Mavolt CIDER – Label</title>
<link href="https://fonts.googleapis.com/css2?family=Cinzel:wght@500;600;700&display=swap" rel="stylesheet">
<style>
  :root {
    --backdrop: #eeece8;
    --label-paper: #ffffff;
    --gold: #b8963e;
    --gold-soft: #c2a35a;
    --apple-light: #f2b8d4;
    --apple-mid: #d85a9c;
    --apple-deep: #9e2c70;
    --leaf: #6cc04a;
  }
  html, body {
    margin: 0;
    padding: 0;
    width: 800px;
    height: 1200px;
    overflow: hidden;
    background: var(--backdrop);
  }
  .canvas {
    position: relative;
    width: 800px;
    height: 1200px;
  }
  .label {
    position: absolute;
    left: 50px;
    top: 200px;
    width: 700px;
    height: 800px;
    background: var(--label-paper);
    box-shadow: 0 2px 10px rgba(0,0,0,0.08);
    font-family: 'Cinzel', serif;
    color: var(--gold);
  }
  .product-name {
    position: absolute;
    top: 28px;
    left: 90px;
    width: 540px;
    margin: 0;
    text-align: center;
    font-weight: 600;
    font-size: 104px;
    letter-spacing: 14px;
    line-height: 1;
    color: var(--gold);
  }
  .brand-mark {
    position: absolute;
    top: 168px;
    left: 190px;
    display: flex;
    align-items: center;
    gap: 10px;
    font-weight: 700;
    font-size: 34px;
    color: var(--gold);
  }
  .brand-dot {
    width: 24px;
    height: 24px;
    border-radius: 50%;
    background: var(--gold);
  }
  .apple-art {
    position: absolute;
    left: 270px;
    top: 250px;
    width: 330px;
    height: 420px;
    border-radius: 4px;
    background: linear-gradient(135deg, var(--apple-light) 0%, var(--apple-mid) 55%, var(--apple-deep) 100%);
  }
  .side-claim {
    position: absolute;
    left: 42px;
    top: 400px;
    transform: translate(-50%, -50%) rotate(-90deg);
    white-space: nowrap;
    font-weight: 600;
    font-size: 44px;
    letter-spacing: 3px;
    line-height: 1;
    color: var(--gold);
  }
  .side-origin {
    position: absolute;
    left: 668px;
    top: 370px;
    transform: translate(-50%, -50%) rotate(90deg);
    white-space: nowrap;
    font-weight: 500;
    font-size: 15px;
    letter-spacing: 1.5px;
    line-height: 1;
    color: var(--gold-soft);
  }
  .volume {
    position: absolute;
    right: 58px;
    top: 690px;
    font-weight: 600;
    font-size: 24px;
    color: var(--gold);
  }
  .tagline {
    position: absolute;
    left: 0;
    top: 744px;
    width: 100%;
    margin: 0;
    text-align: center;
    font-weight: 600;
    font-size: 14px;
    letter-spacing: 1.5px;
    text-transform: uppercase;
    color: var(--gold);
  }
</style>
</head>
<body>
  <div class="canvas">
    <section class="label">
      <h1 class="product-name">CIDER</h1>
      <div class="brand-mark"><span class="brand-dot"></span><span>Mavolt</span></div>

      <div class="apple-art" role="img" aria-label="Faceted low-poly apple illustration in pink and magenta tones with a green leaf"></div>

      <div class="side-claim">APPLE 100% NATURAL</div>
      <div class="side-origin">Harvested and Brewed in HIROSAKI, AOMORI, JAPAN</div>
      <div class="volume">330ml</div>
      <p class="tagline">The Genuine Brisk &amp; Tap Hard Cider Alc.7%</p>
    </section>
  </div>
</body>
</html>
```